Risk Management Company in need of Business Card Design

We sell risk management insurance to Lenders (Banks, Credit Unions, Real Estate Trust).

We need a very clean, professional card that will leave a great impression.

We are looking to use a blue color for our logo on the card (Preferably close to royal blue but are open to looking at navy blue or any darker blues as well).

Please see the logo attached to get an idea. We are open to writing Harbor Vault Under the logo or next to the logo. Really whatever looks best.

Target Market(s)

Banks, Credit Unions, Real Estate Trusts

Industry/Entity Type

Insurance

Contact Information for Business Card

Name: Mark Dunstan
Title: Regional Sales Director
Email: mdunstan@harborvault-example.net
C:555-318-2047
D:555-674-1192
800-555-0147 Ext.312
F:555-829-6630 (We would like to see some cards without the fax number as well to compare)

Company Name: Harbor Vault
Website: www.harborvault-example.net

Address: 418 E. Marlowe St. Suite 140, Towson, MD 21286 (Preferably written on the bottom of the card in small print.)

Colors
0355a3
0455a3

Requirements
Nice to have
• We would like to see a couple of where the back has the logo in reverse colors (Logo White, Background Blue)

```html
<!DOCTYPE html>
<html lang="en">
<head>
<meta charset="utf-8">
<title>Harbor Vault – Business Cards</title>
<link rel="stylesheet" href="https://fonts.googleapis.com/css2?family=Cinzel:wght@500;600&family=Source+Sans+3:wght@400;600;700&display=swap">
<style>
  :root {
    --slate: #2f4b59;
    --royal: #0455a3;
    --white: #ffffff;
    --paper: #ecebe8;
    --contact: #e4ebee;
    --rule-blue: #1560b5;
  }
  * { box-sizing: border-box; margin: 0; padding: 0; }
  html, body { width: 1200px; height: 732px; overflow: hidden; background: var(--paper); }
  .sheet { position: relative; width: 1200px; height: 732px; }

  .card {
    position: absolute; width: 540px; height: 308px; overflow: hidden;
    box-shadow: 0 4px 14px rgba(0,0,0,.18);
  }
  .card--front { left: 40px; top: 40px; background: var(--white); }
  .card--back-blue { left: 620px; top: 40px; background: var(--royal); }
  .card--back-slate { left: 330px; top: 394px; background: var(--slate); }

  .front-panel { position: absolute; inset: 0; }

  .brand-word {
    position: absolute; left: 0; width: 258px; top: 202px;
    text-align: center; white-space: nowrap;
    font-family: "Cinzel", serif; font-weight: 600; font-size: 25px;
    color: var(--slate); letter-spacing: .5px;
  }

  .contact {
    position: absolute; right: 18px; top: 32px; text-align: right;
    font-family: "Source Sans 3", sans-serif; color: var(--contact);
  }
  .contact__name { font-weight: 700; font-size: 19px; color: var(--white); }
  .contact__title { font-size: 13px; margin-top: 2px; }
  .contact__list { list-style: none; margin-top: 20px; font-size: 13px; line-height: 21px; }
  .contact__list li { display: flex; justify-content: flex-end; align-items: center; gap: 6px; white-space: nowrap; }
  .contact__list .ext { font-size: 9px; margin-left: -3px; }
  .contact__list svg { width: 10px; height: 10px; fill: var(--contact); flex: none; }
  .contact__address { margin-top: 12px; font-size: 13px; line-height: 19px; }

  .back-name {
    position: absolute; left: 0; right: 0; top: 108px; text-align: center;
    font-family: "Cinzel", serif; font-weight: 600; font-size: 50px;
    color: var(--white); letter-spacing: 1px;
  }
  .back-url {
    position: absolute; left: 0; right: 0; top: 182px; text-align: center;
    font-family: "Source Sans 3", sans-serif; font-weight: 700; font-size: 16px;
    color: var(--white); letter-spacing: 3px;
  }
</style>
</head>
<body>
<main class="sheet">

  <section class="card card--front" aria-label="Front of business card">
    <svg class="front-panel" viewBox="0 0 540 308" width="540" height="308" aria-hidden="true">
      <path d="M270 0 C302 70 284 140 280 190 C276 250 282 290 288 308 L540 308 L540 0 Z" fill="var(--slate)"/>
      <path d="M260 0 C292 70 274 140 270 190 C266 250 272 290 278 308" fill="none" stroke="var(--rule-blue)" stroke-width="3"/>
    </svg>

    <div class="brand-word">HARBOR VAULT</div>

    <div class="contact">
      <p class="contact__name">Mark Dunstan</p>
      <p class="contact__title">Regional Sales Director</p>
      <ul class="contact__list">
        <li><svg viewBox="0 0 12 12"><path d="M3 1 L5 3.5 L4 5 Q5 7 7 8 L8.5 7 L11 9 L9.5 11 Q2 10 1 2.5 Z"/></svg>555-674-1192</li>
        <li><svg viewBox="0 0 12 12"><path d="M3 1 L5 3.5 L4 5 Q5 7 7 8 L8.5 7 L11 9 L9.5 11 Q2 10 1 2.5 Z"/></svg>800-555-0147 <span class="ext">Ext.312</span></li>
        <li><svg viewBox="0 0 12 12"><rect x="3" y="0.5" width="6" height="11" rx="1.2"/></svg>555-829-6630</li>
        <li><svg viewBox="0 0 12 12"><path d="M0.5 3 L6 7 L11.5 3 V10.5 H0.5 Z M0.5 1.5 H11.5 L6 5.5 Z"/></svg>mdunstan@harborvault-example.net</li>
        <li><svg viewBox="0 0 12 12"><circle cx="6" cy="6" r="5.5"/></svg>www.harborvault-example.net</li>
      </ul>
      <p class="contact__address">418 E. Marlowe St.<br>Suite 140, Towson, MD 21286</p>
    </div>
  </section>

  <section class="card card--back-blue" aria-label="Back of business card, blue">
    <p class="back-name">HARBOR VAULT</p>
    <p class="back-url">www.harborvault-example.net</p>
  </section>

  <section class="card card--back-slate" aria-label="Back of business card, slate">
    <p class="back-name">HARBOR VAULT</p>
    <p class="back-url">www.harborvault-example.net</p>
  </section>

</main>
</body>
</html>
```